Pinecrest Real Estate A5 Flyer

A5 Flyer for print distribution.

Front (include attached photo and branding):
Pinecrest are a new face in the Shelley & Rossmoyne real estate market. The Pinecrest team are both Shelley ‘locals’ and are genuinely and sincerely committed to this community. They put people first and pursue exceptional outcomes for their clients. This is the founding vision of Pinecrest.

Values:
Outstanding Customer Service
Timely Communication
Integrity Always
People First
Exceptional Negotiation

If you’re thinking of selling, interested in a free market appraisal, or simply want to find out more about the Pinecrest team, please reach out to Doug or Rowan for a chat. We’d love to shout you a coffee at The Lantern Coffee + Kitchen.

Pinecrest Real Estate
E: hello@pinecrestrealestate-example.com.au
W: pinecrestrealestate-example.com.au

Back (half the page about Doug, other half the page about Rowan). Please include headshots (Rowan is the younger one):

Rowan Ferrabee (Property Consultant):

Rowan has an in-depth understanding of all things property & finance related. With a degree in property & finance, diploma in finance & mortgage broking, certificate IV in real estate practice, project management roles in residential property development, plus years of small business experience as co-founder/co-owner of The Lantern Coffee + Kitchen, his experience in managing competing demands and complex scenarios runs far and wide.

Rowan also has experience in corporate negotiations which is proving to be a very beneficial skill set. Rowan is deeply committed to people and pursuing exceptional outcomes for his clients. He has built a reputation as a man of his word who is genuine and sincere and willing to go above and beyond for his clients.

rowan@pinecrestrealestate-example.com.au
0412 306 248

Doug Penberthy (Director / Licensee):

Doug has worked in various roles inclusive of being a Real Estate Agent, Bank Manager, Financial Counsellor, Mortgage Broker, and previously a Commercial Pilot. He spent eight years in remote Western Australia, where he worked for an international mining company creating strategies to help support the well-being of employees. Doug’s focus in life has always been to help people. To him, it is always about the relationship. Doug gets enormous satisfaction from seeing individuals, families, and businesses thrive financially. He has become a skilled negotiator with extensive experience working for a number of corporations and private firms.
 
What differentiates Doug is his compassion and commitment to people. He works hard to be an excellent communicator with the aim of achieving great results. He  has extensive sales experience with incredible ability to push the boundaries, think outside the box and meet or surpass expectations. This is why his clients keep coming back and continue to refer well into the future. 

doug@pinecrestrealestate-example.com.au
0438 192 607

Target Market(s)

House Sellers / House Buyers

Industry/Entity Type

Real Estate

Colors
0054AA
0677BA
7BADD7
CADEEF
E8F1F8

Requirements
Must have
• Branding / logo, river photo, head shots, company details etc
Nice to have
• Design as per attached branding guide

```html
<!DOCTYPE html>
<html lang="en">
<head>
<meta charset="utf-8">
<title>Pinecrest Real Estate A5 Flyer</title>
<link href="https://fonts.googleapis.com/css2?family=Manrope:wght@400;500;600;700&display=swap" rel="stylesheet">
<style>
  :root {
    --navy: #18212f;
    --ink: #1f2530;
    --accent: #737b9c;
    --band: #8d92ab;
    --band-light: #c9ccd8;
    --backdrop: #e8e9ec;
    --river-top: #dfe3ea;
    --river-bottom: #34425c;
    --aerial-top: #7d93a8;
    --aerial-bottom: #5a6a55;
    --headshot: #b9bdc6;
  }
  * { box-sizing: border-box; margin: 0; padding: 0; }
  html, body { width: 1050px; height: 1200px; overflow: hidden; }
  body {
    background: var(--backdrop);
    font-family: "Manrope", sans-serif;
    color: var(--ink);
    position: relative;
  }
  .page {
    position: absolute;
    top: 253px;
    width: 490px;
    height: 693px;
    background: linear-gradient(135deg, #ffffff 0%, #f3f4f7 45%, #fbfbfc 70%, #eef0f4 100%);
    box-shadow: 0 6px 18px rgba(0,0,0,0.18);
    overflow: hidden;
  }
  .page--front { left: 20px; }
  .page--back { left: 540px; }

  .page-band {
    position: absolute; left: 0; right: 0; bottom: 0; height: 12px;
    background: linear-gradient(var(--band-light) 0 3px, transparent 3px 5px, var(--band) 5px);
  }

  /* Front */
  .brand { position: absolute; left: 28px; top: 33px; width: 240px; text-align: center; }
  .brand-dot { width: 55px; height: 55px; border-radius: 50%; background: var(--navy); margin: 0 auto 9px; }
  .brand-name { font-size: 17px; font-weight: 500; letter-spacing: 5px; color: var(--navy); }

  .office { position: absolute; left: 295px; top: 51px; font-size: 7.6px; line-height: 16px; font-weight: 500; }
  .office-name { color: var(--accent); font-size: 10px; font-weight: 600; }
  .office-label { color: var(--accent); }

  .intro { position: absolute; left: 28px; top: 203px; width: 252px; font-size: 11.2px; line-height: 16.6px; }
  .intro p { margin-bottom: 15px; }

  .divider { position: absolute; left: 296px; top: 190px; width: 4px; height: 503px; background: var(--navy); }

  .values { position: absolute; left: 321px; top: 252px; }
  .values-title { font-size: 20px; font-weight: 600; color: var(--navy); margin-bottom: 14px; }
  .values-list { list-style: none; font-size: 11px; line-height: 16px; }
  .values-list li { position: relative; padding-left: 11px; margin-bottom: 12px; }
  .values-list li::before { content: ""; position: absolute; left: 1px; top: 7px; width: 3px; height: 3px; border-radius: 50%; background: var(--ink); }

  .cta { position: absolute; left: 313px; top: 500px; width: 160px; font-size: 10.2px; line-height: 16.3px; }
  .cta p { margin-bottom: 12px; }
  .cta .hl { color: var(--accent); }
  .cta strong { font-weight: 700; }

  .river-photo {
    position: absolute; left: 0; top: 430px; width: 296px; height: 248px;
    background: linear-gradient(180deg, rgba(246,247,250,0) 0%, var(--river-top) 10%, var(--river-bottom) 100%);
  }

  /* Back */
  .aerial-photo {
    position: absolute; left: 0; top: 0; width: 490px; height: 238px;
    background: linear-gradient(180deg, var(--aerial-top) 0%, var(--aerial-bottom) 100%);
  }
  .headshot {
    position: absolute; width: 76px; height: 76px; border-radius: 50%;
    border: 3px solid #f4f5f8;
    background: var(--headshot);
  }
  .headshot--rowan { left: 30px; top: 198px; }
  .headshot--doug { left: 253px; top: 198px; }

  .agent { position: absolute; top: 254px; }
  .agent--rowan { left: 28px; width: 200px; }
  .agent--doug { left: 252px; width: 216px; }
  .agent-head { margin-left: 87px; margin-top: -6px; }
  .agent-name { font-size: 14px; font-weight: 600; color: var(--navy); }
  .agent-role { font-size: 8.6px; font-weight: 500; margin-top: 1px; }
  .agent-bio { margin-top: 17px; font-size: 9.2px; line-height: 12.9px; }
  .agent-bio p { margin-bottom: 12px; }
  .agent--rowan .agent-bio { width: 162px; }
  .agent--doug .agent-bio { width: 214px; }
  .agent-email { position: absolute; font-size: 8px; font-weight: 600; }
  .agent-phone { position: absolute; font-size: 15.5px; font-weight: 600; color: var(--navy); letter-spacing: 0.3px; }
  .agent--rowan .agent-email { top: 384px; }
  .agent--rowan .agent-phone { top: 398px; }
  .agent--doug .agent-email { top: 374px; }
  .agent--doug .agent-phone { top: 388px; }
</style>
</head>
<body>

<section class="page page--front">
  <div class="brand">
    <div class="brand-dot"></div>
    <div class="brand-name">PINECREST</div>
  </div>

  <div class="office">
    <div class="office-name">Pinecrest Real Estate</div>
    <div><span class="office-label">E:</span> hello@pinecrestrealestate-example.com.au</div>
    <div><span class="office-label">W:</span> pinecrestrealestate-example.com.au</div>
  </div>

  <div class="intro">
    <p>Pinecrest are a new face in the Shelley &amp; Rossmoyne real estate market. The Pinecrest team are both Shelley ‘locals’ and are genuinely and sincerely committed to this community.</p>
    <p>They put people first and pursue exceptional outcomes for their clients.</p>
    <p>This is the founding vision of Pinecrest.</p>
  </div>

  <div class="river-photo" role="img" aria-label="Aerial photo of the river foreshore with homes along the shore"></div>

  <div class="divider"></div>

  <div class="values">
    <h2 class="values-title">Values:</h2>
    <ul class="values-list">
      <li>Outstanding Customer<br>Service</li>
      <li>Timely Communication</li>
      <li>Integrity Always</li>
      <li>People First</li>
      <li>Exceptional<br>Negotiation</li>
    </ul>
  </div>

  <div class="cta">
    <p>If you’re thinking of selling, interested in a free market appraisal, or simply want to find out more about the <span class="hl">Pinecrest team</span>, please reach out to <strong>DOUG</strong> or <strong>ROWAN</strong> for a chat.</p>
    <p>We’d love to shout you a coffee at The Lantern Coffee + Kitchen.</p>
  </div>

  <div class="page-band"></div>
</section>

<section class="page page--back">
  <div class="aerial-photo" role="img" aria-label="Aerial photo of the riverside suburb with rooftops and trees"></div>

  <div class="headshot headshot--rowan" role="img" aria-label="Headshot of Rowan Ferrabee"></div>
  <div class="headshot headshot--doug" role="img" aria-label="Headshot of Doug Penberthy"></div>

  <article class="agent agent--rowan">
    <div class="agent-head">
      <h3 class="agent-name">Rowan Ferrabee</h3>
      <div class="agent-role">(Property Consultant):</div>
    </div>
    <div class="agent-bio">
      <p>Rowan has an in-depth understanding of all things property &amp; finance related. With a degree in property &amp; finance, diploma in finance &amp; mortgage broking, certificate IV in real estate practice, project management roles in residential property development, plus years of small business experience as co-founder/co-owner of The Lantern Coffee + Kitchen, his experience in managing competing demands and complex scenarios runs far and wide.</p>
      <p>Rowan also has experience in corporate negotiations which is proving to be a very beneficial skill set. Rowan is deeply committed to people and pursuing exceptional outcomes for his clients. He has built a reputation as a man of his word who is genuine and sincere and willing to go above and beyond for his clients.</p>
    </div>
    <div class="agent-email">rowan@pinecrestrealestate-example.com.au</div>
    <div class="agent-phone">0412 306 248</div>
  </article>

  <article class="agent agent--doug">
    <div class="agent-head">
      <h3 class="agent-name">Doug Penberthy</h3>
      <div class="agent-role">(Director / Licensee):</div>
    </div>
    <div class="agent-bio">
      <p>Doug has worked in various roles inclusive of being a Real Estate Agent, Bank Manager, Financial Counsellor, Mortgage Broker, and previously a Commercial Pilot. He spent eight years in remote Western Australia, where he worked for an international mining company creating strategies to help support the well-being of employees. Doug’s focus in life has always been to help people. To him, it is always about the relationship. Doug gets enormous satisfaction from seeing individuals, families, and businesses thrive financially. He has become a skilled negotiator with extensive experience working for a number of corporations and private firms.</p>
      <p>What differentiates Doug is his compassion and commitment to people. He works hard to be an excellent communicator with the aim of achieving great results. He has extensive sales experience with incredible ability to push the boundaries, think outside the box and meet or surpass expectations. This is why his clients keep coming back and continue to refer well into the future.</p>
    </div>
    <div class="agent-email">doug@pinecrestrealestate-example.com.au</div>
    <div class="agent-phone">0438 192 607</div>
  </article>

  <div class="page-band"></div>
</section>

</body>
</html>
```